eFlyer for Banner Page for Facebook, Twitter and YouTube

We need facebook design for announcing the ministry's theme for 2015. (For my organization's background information please see my FB Community page entitled: Evangelist Mirela Pastwick Ministries.) The project is as follows: Create the 2015 eFlyer/FB Banner Page that has the following information. 1) Evangelist Mirela Pastwick Ministires; 2) 2015; 3) Triumphant! (see the attached eflyer from 2014). Thank you.

Industry/Entity Type

Ministry

```html
<!DOCTYPE html>
<html lang="en">
<head>
<meta charset="utf-8">
<title>Triumphant! — Evangelist Mirela Pastwick Ministries 2015</title>
<link href="https://fonts.googleapis.com/css2?family=Montserrat:wght@500;800&family=Pinyon+Script&display=swap" rel="stylesheet">
<style>
  :root {
    --sky-blue: #3f5fc8;
    --sky-violet: #8a4fc2;
    --sky-pink: #d86aa8;
    --sky-orange: #f29a5c;
    --sky-gold: #f7c05a;
    --ground-dark: #2a1420;
    --ground-mid: #4a2330;
    --reflect-orange: #e0783a;
    --reflect-pink: #b2587a;
    --deep: #1c0d18;
    --portrait-dark: #2b2230;
    --portrait-warm: #6b4a55;
    --ink: #0b0b0b;
    --white: #ffffff;
  }
  * { margin: 0; padding: 0; box-sizing: border-box; }
  html, body { width: 1200px; height: 1200px; overflow: hidden; background: var(--deep); }
  .flyer { position: relative; width: 1200px; height: 1200px; overflow: hidden; }

  .scenery {
    position: absolute; inset: 0;
    background:
      radial-gradient(ellipse 70% 14% at 55% 58%, rgba(247,192,90,.85), transparent 70%),
      linear-gradient(180deg,
        var(--sky-blue) 0%,
        var(--sky-violet) 12%,
        var(--sky-pink) 26%,
        var(--sky-orange) 40%,
        var(--sky-gold) 52%,
        var(--ground-mid) 56%,
        var(--ground-dark) 66%,
        var(--reflect-pink) 72%,
        var(--reflect-orange) 80%,
        var(--ground-mid) 88%,
        var(--deep) 100%);
  }

  .portrait {
    position: absolute; left: 0; top: 0; width: 425px; height: 650px;
    background:
      radial-gradient(ellipse 45% 30% at 50% 28%, var(--portrait-warm), transparent 75%),
      linear-gradient(180deg, rgba(43,34,48,.55) 0%, var(--portrait-dark) 55%, rgba(43,34,48,0) 100%);
    -webkit-mask-image: radial-gradient(ellipse 75% 70% at 45% 45%, #000 55%, transparent 100%);
            mask-image: radial-gradient(ellipse 75% 70% at 45% 45%, #000 55%, transparent 100%);
  }

  .theme {
    position: absolute; left: 40px; top: 532px; width: 1120px;
    font-family: "Montserrat", sans-serif; font-weight: 800;
    font-size: 146px; line-height: 1; letter-spacing: 1px;
    color: var(--ink); white-space: nowrap;
  }

  .ministry-label {
    position: absolute; left: 156px; top: 682px;
    font-family: "Montserrat", sans-serif; font-weight: 500;
    font-size: 29px; letter-spacing: 3px; color: var(--white);
  }
  .ministry-name {
    position: absolute; left: 490px; top: 690px;
    font-family: "Pinyon Script", cursive; font-size: 96px; line-height: 1;
    color: var(--white); white-space: nowrap;
  }
  .ministry-suffix {
    position: absolute; left: 764px; top: 796px;
    font-family: "Montserrat", sans-serif; font-weight: 500;
    font-size: 28px; letter-spacing: 3px; color: var(--white);
  }

  .year {
    position: absolute; left: 0; width: 1200px; top: 1018px; text-align: center;
    font-family: "Pinyon Script", cursive; font-size: 104px; line-height: 1;
    color: var(--white); padding-right: 90px;
  }
</style>
</head>
<body>
  <main class="flyer">
    <div class="scenery" role="img" aria-label="Sunset sky with pink and orange clouds over a dark rocky landscape reflected in still water"></div>
    <div class="portrait" role="img" aria-label="Portrait of the evangelist in a dark blouse, looking upward"></div>

    <h1 class="theme">TRIUMPHANT!</h1>

    <p class="ministry-label">EVANGELIST</p>
    <p class="ministry-name">Mirela Pastwick</p>
    <p class="ministry-suffix">MINISTRIES</p>

    <p class="year">2015 ; 3</p>
  </main>
</body>
</html>
```